Bright Lanterns Business Card

Design of business cards

Target Market(s)

We are aiming as small business owners who need anything from basic business structures, website plans, business processes and quality assurance.

Industry/Entity Type

Business

Colors

Designer to choose colors to be used in the design.

Requirements
Nice to have
• I would prefer one side of the card to use the green from the logo. Prefer to have the same font as the logo.

```html
<!DOCTYPE html>
<html lang="en">
<head>
<meta charset="utf-8">
<title>Bright Lanterns Consulting – Business Card</title>
<link rel="stylesheet" href="https://fonts.googleapis.com/css2?family=Cinzel:wght@400;600&family=Open+Sans:wght@300;400&display=swap">
<style>
  :root {
    --page: #ecebe7;
    --slate-dark: #4a4b4d;
    --slate-mid: #76777a;
    --slate-light: #9a9b9e;
    --lime: #b9dc3c;
    --lime-bright: #d3ef6a;
    --lime-deep: #9cc42a;
    --paper: #ffffff;
    --ink-soft: #5b6b1c;
  }
  * { margin: 0; padding: 0; box-sizing: border-box; }
  html, body { width: 1200px; height: 1023px; overflow: hidden; }
  body {
    background: var(--page);
    position: relative;
    font-family: "Open Sans", Arial, sans-serif;
  }
  .card {
    position: absolute;
    left: 195px;
    width: 810px;
    height: 450px;
    overflow: hidden;
    box-shadow: 0 10px 30px rgba(0,0,0,0.18);
    background: radial-gradient(ellipse at 35% 45%, var(--slate-light) 0%, var(--slate-mid) 45%, var(--slate-dark) 100%);
  }
  .card--front { top: 45px; }
  .card--back { top: 528px; }

  .front-shape { position: absolute; inset: 0; width: 100%; height: 100%; }

  .brand {
    position: absolute;
    display: flex;
    align-items: center;
    gap: 16px;
  }
  .brand-mark {
    width: 18px; height: 18px;
    border-radius: 50%;
    background: var(--lime);
    flex: none;
  }
  .brand-name {
    font-family: "Cinzel", "Times New Roman", serif;
    font-weight: 400;
    color: var(--paper);
    line-height: 1.05;
    letter-spacing: 1px;
  }
  .card--front .brand { left: 48px; top: 70px; }
  .card--front .brand-name { font-size: 34px; }
  .card--back .brand { left: 150px; top: 150px; }
  .card--back .brand-name { font-size: 44px; }

  .person {
    position: absolute;
    left: 48px;
    top: 290px;
  }
  .person-name {
    font-family: "Cinzel", "Times New Roman", serif;
    font-size: 30px;
    color: var(--lime);
    letter-spacing: 1px;
  }
  .person-phone {
    margin-top: 6px;
    font-size: 22px;
    font-weight: 300;
    color: var(--paper);
    letter-spacing: 2px;
  }

  .contact {
    position: absolute;
    right: 40px;
    bottom: 46px;
    text-align: right;
    font-size: 19px;
    font-weight: 400;
    color: var(--ink-soft);
    line-height: 1.55;
    letter-spacing: 0.5px;
  }

  .social {
    position: absolute;
    right: 28px;
    top: 24px;
    display: flex;
    gap: 10px;
  }
  .social-square {
    width: 20px; height: 20px;
    border-radius: 3px;
    background: rgba(255,255,255,0.45);
  }
</style>
</head>
<body>

<section class="card card--front" aria-label="Business card front">
  <svg class="front-shape" viewBox="0 0 810 450" preserveAspectRatio="none" aria-hidden="true">
    <defs>
      <linearGradient id="limeFill" x1="0" y1="0" x2="1" y2="1">
        <stop offset="0" stop-color="var(--lime-bright)"/>
        <stop offset="0.55" stop-color="var(--lime)"/>
        <stop offset="1" stop-color="var(--lime-deep)"/>
      </linearGradient>
    </defs>
    <path d="M400 0 C 540 120, 360 300, 480 450 L810 450 L810 0 Z" fill="url(#limeFill)"/>
    <path d="M400 0 C 540 120, 360 300, 480 450" fill="none" stroke="var(--paper)" stroke-width="7"/>
  </svg>

  <div class="brand">
    <span class="brand-mark"></span>
    <div class="brand-name">Bright<br>Lanterns<br>Consulting</div>
  </div>

  <div class="person">
    <div class="person-name">Maren Whitlock</div>
    <div class="person-phone">0412 555 019</div>
  </div>

  <div class="contact">
    <div>maren@brightlanterns.com.au</div>
    <div>www.brightlanterns.com.au</div>
  </div>

  <div class="social" aria-hidden="true">
    <span class="social-square"></span>
    <span class="social-square"></span>
  </div>
</section>

<section class="card card--back" aria-label="Business card back">
  <div class="brand">
    <span class="brand-mark"></span>
    <div class="brand-name">Bright<br>Lanterns<br>Consulting</div>
  </div>
</section>

</body>
</html>
```